Tallow Crest Business Card

We need a business card designed for a a company called "Tallow Crest". We offer consulting, coaching and training to business leaders and coaches (across the world) using the latest findings in neuroscience, social and emotional intelligence and positive psychology. The final design should communicate the use of brain science to create sustainable relationships.

The card should be doublesided. The logo is attached and names and titles will be provided to the successful designer. Thank you.

Industry/Entity Type

Training

```html
<!DOCTYPE html>
<html lang="en">
<head>
<meta charset="utf-8">
<title>Tallow Crest Business Card</title>
<link rel="stylesheet" href="https://fonts.googleapis.com/css2?family=Open+Sans:wght@400;700&display=swap">
<style>
  :root {
    --teal: #0b7d9b;
    --teal-dark: #086a85;
    --lime: #b5d62a;
    --white: #ffffff;
    --ink: #5c5f63;
    --backdrop: #e9ebec;
    --card-w: 700px;
    --card-h: 400px;
  }
  * { box-sizing: border-box; margin: 0; padding: 0; }
  html, body {
    width: 1200px; height: 900px; overflow: hidden;
    background: var(--backdrop);
    font-family: "Open Sans", Arial, sans-serif;
  }
  .canvas { position: relative; width: 1200px; height: 900px; }
  .card {
    position: absolute; left: 250px;
    width: var(--card-w); height: var(--card-h);
    border-radius: 18px; overflow: hidden;
    box-shadow: 0 6px 18px rgba(0,0,0,.18);
  }
  /* Back side */
  .card-back { top: 40px; background: var(--teal); color: var(--white); }
  .back-brand {
    position: absolute; top: 150px; left: 0; right: 0;
    display: flex; justify-content: center; align-items: center; gap: 14px;
  }
  .brand-dot { width: 22px; height: 22px; border-radius: 50%; background: var(--lime); }
  .back-brand .brand-name { font-size: 44px; font-weight: 700; color: var(--white); }
  .back-url {
    position: absolute; bottom: 52px; left: 0; right: 0; text-align: center;
    font-size: 18px; color: var(--lime);
  }
  /* Front side */
  .card-front { top: 470px; background: var(--white); }
  .front-wave { position: absolute; inset: 0; }
  .front-brand {
    position: absolute; left: 40px; top: 105px; width: 290px;
    display: flex; align-items: center; gap: 12px;
  }
  .front-brand .brand-name { font-size: 38px; font-weight: 700; color: var(--teal); }
  .divider {
    position: absolute; left: 355px; top: 60px; width: 1px; height: 220px;
    background: linear-gradient(to bottom, rgba(90,90,90,0), rgba(90,90,90,.6), rgba(90,90,90,0));
  }
  .contact { position: absolute; left: 390px; top: 70px; color: var(--ink); }
  .contact-name { font-size: 24px; font-weight: 700; color: var(--teal); line-height: 1.1; }
  .contact-title { font-size: 16px; margin-bottom: 18px; }
  .contact-address { font-size: 15px; line-height: 1.35; margin-bottom: 10px; }
  .contact-list { list-style: none; font-size: 15px; line-height: 1.5; }
  .contact-list li { display: flex; align-items: center; gap: 9px; }
  .contact-list svg { width: 14px; height: 14px; fill: var(--teal); flex: none; }
</style>
</head>
<body>
<main class="canvas">
  <section class="card card-back" aria-label="Card back">
    <div class="back-brand">
      <span class="brand-dot"></span>
      <span class="brand-name">Tallow Crest</span>
    </div>
    <p class="back-url">www.tallowcrest.com</p>
  </section>

  <section class="card card-front" aria-label="Card front">
    <svg class="front-wave" viewBox="0 0 700 400" preserveAspectRatio="none" aria-hidden="true">
      <path d="M0,262 C150,256 270,335 460,372 C570,392 650,388 700,384 L700,400 L0,400 Z" fill="var(--teal)"/>
      <path d="M0,248 C160,242 280,322 465,358 C575,378 650,372 700,366" fill="none" stroke="var(--lime)" stroke-width="4"/>
    </svg>
    <div class="front-brand">
      <span class="brand-name">Tallow Crest</span>
    </div>
    <div class="divider"></div>
    <div class="contact">
      <p class="contact-name">Daniel Harrow</p>
      <p class="contact-title">Marketing Manager</p>
      <p class="contact-address">PO Box 718<br>Fernvale SA 5190</p>
      <ul class="contact-list">
        <li><svg viewBox="0 0 16 16"><path d="M3 1h3l1.5 4-2 1.2a9 9 0 0 0 4.3 4.3L11 8.5l4 1.5v3a2 2 0 0 1-2 2A13 13 0 0 1 1 3a2 2 0 0 1 2-2z"/></svg>(08) 5550 4127</li>
        <li><svg viewBox="0 0 16 16"><path d="M4 0h8a1 1 0 0 1 1 1v14a1 1 0 0 1-1 1H4a1 1 0 0 1-1-1V1a1 1 0 0 1 1-1zm1 2v10h6V2zm3 11a1 1 0 1 0 0 2 1 1 0 0 0 0-2z"/></svg>0400 555 382</li>
        <li><svg viewBox="0 0 16 16"><path d="M0 3h16v10H0zm1.5 1.2V12h13V4.2L8 9z"/></svg>daniel@tallowcrest.com</li>
        <li><svg viewBox="0 0 16 16"><path d="M8 0a8 8 0 1 0 0 16A8 8 0 0 0 8 0zm0 1.5c.9 0 2 2 2.3 5H5.7C6 3.5 7.1 1.5 8 1.5zM1.6 9.5h2.6a13 13 0 0 0 1 4.4 6.5 6.5 0 0 1-3.6-4.4zm0-3a6.5 6.5 0 0 1 3.6-4.4 13 13 0 0 0-1 4.4zm6.4 8c-.9 0-2-2-2.3-5h4.6c-.3 3-1.4 5-2.3 5zm2.8-.6a13 13 0 0 0 1-4.4h2.6a6.5 6.5 0 0 1-3.6 4.4zm1-7.4a13 13 0 0 0-1-4.4 6.5 6.5 0 0 1 3.6 4.4z"/></svg>www.tallowcrest.com</li>
      </ul>
    </div>
  </section>
</main>
</body>
</html>
```